Business Card cabinets and cabinets components making company.

the card should be formal and interesting at the same time. The main colors will be black and white.

Font styles to use
Sans Serif

Colors

Designer to choose only greyscale colors for use in the design.

Requirements
Must have
• At least must have the followings:
office phone
cell phone
address
position
name
email
web

```html
<!DOCTYPE html>
<html lang="en">
<head>
<meta charset="utf-8">
<title>Joinwell Business Card</title>
<link rel="stylesheet" href="https://fonts.googleapis.com/css2?family=Roboto+Condensed:wght@400;700&display=swap">
<style>
  :root {
    --backdrop: #e6e3e3;
    --ink: #0a0a0a;
    --paper: #ffffff;
    --mark-grey: #4a4a4a;
    --rule-grey: #6e6e6e;
    --shadow: rgba(0, 0, 0, 0.18);
  }
  * { box-sizing: border-box; margin: 0; padding: 0; }
  html, body {
    width: 1200px;
    height: 849px;
    overflow: hidden;
    background: var(--backdrop);
    font-family: "Roboto Condensed", "Arial Narrow", sans-serif;
  }
  .sheet {
    position: relative;
    width: 1200px;
    height: 849px;
  }
  .card {
    position: absolute;
    top: 270px;
    width: 525px;
    height: 300px;
    overflow: hidden;
    box-shadow: 0 6px 18px var(--shadow);
  }
  /* Front */
  .card--front {
    left: 50px;
    background: var(--ink);
    display: flex;
    align-items: center;
    justify-content: center;
  }
  .front-mark {
    display: flex;
    align-items: center;
    gap: 16px;
    color: var(--mark-grey);
    font-size: 76px;
    font-weight: 700;
    letter-spacing: 1px;
  }
  .front-mark__square {
    width: 40px;
    height: 40px;
    background: var(--mark-grey);
  }
  /* Back */
  .card--back {
    left: 625px;
    display: grid;
    grid-template-columns: 59% 41%;
    background: var(--paper);
  }
  .back-identity {
    position: relative;
    padding: 70px 20px 0 40px;
    color: var(--ink);
  }
  .back-identity__name {
    font-size: 23px;
    font-weight: 700;
    line-height: 1.15;
  }
  .back-identity__position {
    font-size: 22px;
    font-weight: 400;
    line-height: 1.2;
  }
  .back-brand {
    position: absolute;
    left: 40px;
    bottom: 40px;
    display: flex;
    align-items: center;
    gap: 7px;
    font-size: 27px;
    font-weight: 700;
    color: var(--ink);
  }
  .back-brand__square {
    width: 14px;
    height: 14px;
    background: var(--ink);
  }
  .back-contact {
    background: var(--ink);
    color: var(--paper);
    padding: 58px 18px 0 26px;
    font-size: 15.5px;
    line-height: 1.32;
  }
  .back-contact__address { margin-bottom: 30px; }
  .back-contact__web { font-weight: 700; }
</style>
</head>
<body>
  <main class="sheet">
    <section class="card card--front" aria-label="Card front">
      <div class="front-mark">
        <span class="front-mark__square"></span>
        <span class="front-mark__name">Joinwell</span>
      </div>
    </section>

    <section class="card card--back" aria-label="Card back">
      <div class="back-identity">
        <p class="back-identity__name">Firstname Surname</p>
        <p class="back-identity__position">Position</p>
        <div class="back-brand">
          <span class="back-brand__square"></span>
          <span class="back-brand__name">Joinwell</span>
        </div>
      </div>
      <div class="back-contact">
        <address class="back-contact__address" style="font-style: normal;">
          Business address line 1<br>
          Business address line 2<br>
          Business address line 3<br>
          ZIP CODE
        </address>
        <p class="back-contact__office">0123 456 7890</p>
        <p class="back-contact__mobile">0123 456 7890</p>
        <p class="back-contact__email">fsurname@joinwell.com</p>
        <p class="back-contact__web">www.joinwell.com</p>
      </div>
    </section>
  </main>
</body>
</html>
```